Website Redesign for Accommodation Directory

We need a redesign for bluepinelodgefinder.example
The new design needs to include a banner with overlaid text and a 'get started now' button. The overlaid text could be 'Find Hotels in Auckland, New Zealand' for example.
The new design needs to include:
- primary navigation in header
- an accommodation search (left or right column)
- a secondary navigation menu (under the search).
We will need the following font styles (including links for each) defined also please:
h1, h2, h3, h4, h5, h6, p, ul, ol, address, pre

```html
<!DOCTYPE html>
<html lang="en">
<head>
<meta charset="utf-8">
<title>Blue Pine Lodge Finder</title>
<link href="https://fonts.googleapis.com/css2?family=Open+Sans:wght@400;600;700;800&family=Ubuntu:wght@400;500&display=swap" rel="stylesheet">
<style>
  :root {
    --page-bg: #ebebeb;
    --bar-bg: #595a5c;
    --bar-text: #f2f2f2;
    --brand-red: #e3202a;
    --text-dark: #1e1e1e;
    --text-mid: #555557;
    --panel-bg: #e4e4e4;
    --panel-line: #d2d2d2;
    --banner-dark: #3c3d3f;
    --banner-light: #5b5c5e;
    --map-sea: #6d93ba;
    --white: #ffffff;
  }
  * { box-sizing: border-box; margin: 0; padding: 0; }
  html, body { width: 1200px; height: 920px; overflow: hidden; }
  body {
    background: var(--page-bg);
    font-family: "Open Sans", sans-serif;
    color: var(--text-dark);
    position: relative;
  }
  a { color: inherit; text-decoration: none; }

  .utility-bar {
    position: absolute; left: 0; top: 0; width: 1200px; height: 33px;
    background: var(--bar-bg);
  }
  .utility-links {
    position: absolute; right: 160px; top: 6px;
    font-family: "Ubuntu", sans-serif; font-size: 15px; color: var(--bar-text);
  }

  .site-brand {
    position: absolute; left: 161px; top: 82px;
    display: flex; align-items: center; gap: 8px;
  }
  .brand-square { width: 42px; height: 42px; background: var(--brand-red); }
  .brand-name { font-size: 31px; font-weight: 400; color: var(--text-mid); letter-spacing: -0.5px; }

  .primary-nav {
    position: absolute; right: 161px; top: 118px;
    font-size: 15.5px; color: var(--text-dark);
  }
  .primary-nav .sep { margin: 0 12px; }

  .hero {
    position: absolute; left: 161px; top: 150px; width: 878px; height: 258px;
    background: radial-gradient(ellipse at 35% 40%, var(--banner-light), var(--banner-dark));
  }
  .hero-title {
    position: absolute; left: 29px; top: 52px; width: 405px;
    font-size: 26px; font-weight: 800; line-height: 38px; color: var(--white);
    white-space: nowrap; letter-spacing: -0.2px;
    text-transform: uppercase; text-shadow: 0 2px 3px rgba(0,0,0,.5);
  }
  .hero-button {
    position: absolute; left: 198px; top: 158px; width: 168px; height: 41px;
    background: linear-gradient(#d91a1a, #b30d0d); border: 1px solid #f2d2d2;
    color: var(--white); font-family: "Ubuntu", sans-serif; font-size: 21px;
    display: flex; align-items: center; justify-content: center;
  }
  .hero-map {
    position: absolute; left: 440px; top: 8px; width: 430px; height: 242px;
    background: var(--map-sea);
  }

  .welcome {
    position: absolute; left: 161px; top: 432px; width: 627px;
  }
  .welcome h1 { font-size: 26px; font-weight: 400; color: var(--text-mid); }
  .welcome h1 span { color: var(--brand-red); }
  .welcome .lead {
    margin-top: 13px; font-size: 18.6px; line-height: 26.5px; text-align: justify;
  }
  .welcome .body {
    margin-top: 13px; font-size: 11.2px; line-height: 16px; text-align: justify;
  }

  .categories {
    position: absolute; left: 161px; top: 745px; width: 629px; height: 121px;
    background: var(--panel-bg); padding: 6px 7px;
  }
  .categories h2 { font-size: 15.5px; font-weight: 400; color: var(--brand-red); }
  .category-list {
    list-style: none; margin-top: 5px;
    display: grid; grid-template-columns: 254px 265px auto; row-gap: 6px;
    font-size: 11.5px; font-weight: 600; letter-spacing: .4px;
  }
  .category-list li { display: flex; align-items: center; gap: 2px; height: 15px; }
  .category-list svg { width: 8px; height: 9px; }

  .side-panel {
    position: absolute; left: 809px; width: 230px; background: var(--panel-bg);
  }
  .side-panel h3 {
    font-size: 16px; font-weight: 600; color: var(--text-mid); white-space: nowrap;
    border-bottom: 1px solid var(--panel-line); padding: 10px 0 5px 8px;
    letter-spacing: -0.2px;
  }
  .search-panel { top: 439px; height: 150px; }
  .contact-panel { top: 624px; height: 242px; }
  .contact-panel h3 { text-align: center; padding-left: 0; font-size: 17.5px; }
  .field {
    display: block; margin-left: 14px; background: var(--white);
    border: 1px solid #d6d6d6; font-size: 10px; color: #444; letter-spacing: .5px;
    padding: 1px 4px; height: 16px;
  }
  .select { width: 198px; position: relative; }
  .select svg { position: absolute; right: 4px; top: 6px; width: 7px; height: 4px; }
  .search-panel .select:first-of-type { margin-top: 12px; }
  .search-panel .select + .select { margin-top: 10px; }
  .contact-panel .field { width: 204px; margin-top: 12px; }
  .contact-panel .field:first-of-type { margin-top: 10px; }
  .contact-panel .message { height: 69px; margin-top: 12px; padding-top: 3px; }
  .dark-button {
    position: absolute; right: 18px; width: 89px; height: 32px;
    background: linear-gradient(#3b3b3b, #151515); border: 2px solid #9c9c9c;
    color: var(--white); font-family: "Ubuntu", sans-serif; font-size: 21px;
    display: flex; align-items: center; justify-content: center;
  }
  .search-panel .dark-button { top: 105px; }
  .contact-panel .dark-button { top: 202px; right: 14px; }

  .site-footer {
    position: absolute; left: 0; top: 886px; width: 1200px; height: 34px;
    background: var(--bar-bg); color: #dcdcdc; font-size: 11.5px;
    display: flex; align-items: center; justify-content: center; letter-spacing: .2px;
  }
</style>
</head>
<body>
  <div class="utility-bar">
    <nav class="utility-links"><a href="#">Free Insurance Quotes</a> | <a href="#">Free Website Statistics</a> | <a href="#">Company Reviews</a></nav>
  </div>

  <header class="site-brand">
    <span class="brand-square"></span>
    <span class="brand-name">bluepinelodgefinder</span>
  </header>

  <nav class="primary-nav">
    <a href="#">Supplier</a><span class="sep">|</span><a href="#">Login Add Your Property</a><span class="sep">|</span><a href="#">Home</a>
  </nav>

  <section class="hero">
    <h2 class="hero-title">Find Hotels in Auckland,<br>New Zealand</h2>
    <a class="hero-button" href="#">Get Started Now</a>
    <div class="hero-map" role="img" aria-label="World map with continents and oceans labelled, Oceania highlighted"></div>
  </section>

  <main class="welcome">
    <h1><span>Welcome To</span> Blue Pine Lodge Finder</h1>
    <p class="lead">You’ve come to the right place to find Accommodation in Any Country whether it’s a hotel, motel, backpackers, bed and breakfast or beach house you're after you'll find just what you need to enjoy your stay in Any Country.</p>
    <p class="body">With much to choose from you'll want to find a place that meets your needs. Our accommodation search tool will help you find the perfect place, regardless of what your price, location or style requirements might be.</p>
    <p class="body">Our Any Country accommodation directory is perfect for times when you’ve scored cheap flights, desperately need last-minute accommodation or are just planning your next holiday or business trip to Any Country.</p>
    <p class="body">With a great selection of Accommodation options in Any Country from cheap nights staying in budget accommodation to 5-star luxury Any Country hotels, so you can really treat yourself, you’ll find it all here.</p>
  </main>

  <section class="categories">
    <h2>Ready to get started? Find Accommodation in Any Country online now.</h2>
    <ul class="category-list">
      <li><svg viewBox="0 0 8 9"><path d="M1 1l5 3.5L1 8" fill="none" stroke="#e3202a" stroke-width="2"/></svg><a href="#">Apartments</a></li>
      <li><svg viewBox="0 0 8 9"><path d="M1 1l5 3.5L1 8" fill="none" stroke="#e3202a" stroke-width="2"/></svg><a href="#">Backpackers</a></li>
      <li><svg viewBox="0 0 8 9"><path d="M1 1l5 3.5L1 8" fill="none" stroke="#e3202a" stroke-width="2"/></svg><a href="#">Batch</a></li>
      <li><svg viewBox="0 0 8 9"><path d="M1 1l5 3.5L1 8" fill="none" stroke="#e3202a" stroke-width="2"/></svg><a href="#">Beach House</a></li>
      <li><svg viewBox="0 0 8 9"><path d="M1 1l5 3.5L1 8" fill="none" stroke="#e3202a" stroke-width="2"/></svg><a href="#">Bed &amp; Breakfast</a></li>
      <li><svg viewBox="0 0 8 9"><path d="M1 1l5 3.5L1 8" fill="none" stroke="#e3202a" stroke-width="2"/></svg><a href="#">Camping Sites</a></li>
      <li><svg viewBox="0 0 8 9"><path d="M1 1l5 3.5L1 8" fill="none" stroke="#e3202a" stroke-width="2"/></svg><a href="#">Caravan Park</a></li>
      <li><svg viewBox="0 0 8 9"><path d="M1 1l5 3.5L1 8" fill="none" stroke="#e3202a" stroke-width="2"/></svg><a href="#">Holiday Homes</a></li>
      <li><svg viewBox="0 0 8 9"><path d="M1 1l5 3.5L1 8" fill="none" stroke="#e3202a" stroke-width="2"/></svg><a href="#">Hostels</a></li>
      <li><svg viewBox="0 0 8 9"><path d="M1 1l5 3.5L1 8" fill="none" stroke="#e3202a" stroke-width="2"/></svg><a href="#">Hotels</a></li>
      <li><svg viewBox="0 0 8 9"><path d="M1 1l5 3.5L1 8" fill="none" stroke="#e3202a" stroke-width="2"/></svg><a href="#">Lodges</a></li>
      <li><svg viewBox="0 0 8 9"><path d="M1 1l5 3.5L1 8" fill="none" stroke="#e3202a" stroke-width="2"/></svg><a href="#">Motels</a></li>
    </ul>
  </section>

  <aside class="side-panel search-panel">
    <h3>ACCOMMODATION SEARCH</h3>
    <div class="field select">All Countries<svg viewBox="0 0 7 4"><path d="M0 0h7L3.5 4z" fill="#222"/></svg></div>
    <div class="field select">All Categories<svg viewBox="0 0 7 4"><path d="M0 0h7L3.5 4z" fill="#222"/></svg></div>
    <a class="dark-button" href="#">Search</a>
  </aside>

  <aside class="side-panel contact-panel">
    <h3>CONTACT US</h3>
    <div class="field">Name:</div>
    <div class="field">Phone:</div>
    <div class="field">Email:</div>
    <div class="field message">Message:</div>
    <a class="dark-button" href="#">Submit</a>
  </aside>

  <footer class="site-footer">© 2011 Blue Pine Lodge Finder | Find Accommodation in Any Country - Accommodation Any Country | Recommend us | Contact Us | Sitemap</footer>
</body>
</html>
```